Yacht Management in Miami & Ft Lauderdale (2019Q2)

I’m looking for a flyer to leave places for people to get information about my company and what services we offer.
We offer monthly management plans to ensure the vessel is ready to go at a moments notice. This can be as simple as washing once a week, or as involved as washing, waxing, detailing, provisioning, and crew services.
We also offer bespoke customizations; stereos, on board WiFi, and engineering.

Target Market(s)

Yacht and boat owners.

Font styles to use
Sans Serif

Colors
87d0c7
85cae6
85acd3
cedeed
cee9f5
cfeae6
0455a3

Requirements
Must have
• Must have simple attention grabbing, without being obnoxious.
• Prefer a 3in x 5in post card size. other size may be an option.
• Must be front and back.
Nice to have
• Languages: English, Spanish, Russian
• USA flag logo
Should not have
• Should not have a lot of text. Icons and photos are great.

```html
<!DOCTYPE html>
<html lang="en">
<head>
<meta charset="utf-8">
<title>Harbor Mates – Postcard Front &amp; Back</title>
<link rel="stylesheet" href="https://fonts.googleapis.com/css2?family=Lato:wght@300;400;700;900&display=swap">
<style>
  :root{
    --red:#e41f26;
    --red-dark:#a8141a;
    --black:#111111;
    --white:#ffffff;
    --stage:#e6e6e4;
    --logo-top:#ffffff;
    --logo-bottom-front:#e86a6e;
    --logo-bottom-back:#555555;
  }
  *{box-sizing:border-box;margin:0;padding:0}
  html,body{width:1200px;height:1200px;overflow:hidden}
  body{background:var(--stage);font-family:'Lato',sans-serif;position:relative;color:var(--white)}

  .postcard{position:absolute;width:1070px;height:642px;transform:scale(0.8);transform-origin:0 0;overflow:hidden;box-shadow:0 6px 18px rgba(0,0,0,.35)}
  .postcard--front{left:90px;top:44px}
  .postcard--back{left:220px;top:586px}

  .postcard__shapes{position:absolute;inset:0;width:1070px;height:642px}
  .postcard__photo{position:absolute;inset:0}
  .postcard--front .postcard__photo{
    clip-path:polygon(908px 0,1070px 0,1070px 642px,445px 642px);
    background:linear-gradient(160deg,#8f9aa3 0%,#c9b9a2 30%,#e6cfb2 48%,#b79c80 65%,#5f6870 85%,#3d4a57 100%);
  }
  .postcard--back .postcard__photo{
    clip-path:polygon(940px 0,1070px 0,1070px 642px,470px 642px);
    background:linear-gradient(175deg,#4c5249 0%,#575c52 45%,#d9dcde 62%,#8a8e90 75%,#8c4a3c 90%,#6e3a30 100%);
  }

  .brand-block{position:absolute;left:20px;top:0;width:162px;height:265px;display:flex;flex-direction:column;align-items:center;justify-content:center}
  .postcard--front .brand-block{background:linear-gradient(180deg,var(--logo-top) 55%,var(--logo-bottom-front) 100%)}
  .postcard--back .brand-block{background:linear-gradient(180deg,var(--logo-top) 45%,var(--logo-bottom-back) 100%)}
  .brand-block__name{font-weight:900;font-size:34px;line-height:1.05;color:var(--black);text-align:center;letter-spacing:.5px}

  .headline-line{position:absolute;text-align:center;white-space:nowrap}
  .headline-line--main{font-weight:900;line-height:1;text-transform:uppercase}
  .headline-line--sub{font-weight:900;line-height:1;text-transform:uppercase}
  .headline-line--tag{font-weight:400}
  .dotted-rule{position:absolute;height:0;border-top:4px dotted var(--white)}

  .service-24{position:absolute;left:736px;top:12px;text-align:center;line-height:.95}
  .service-24__num{font-weight:900;font-size:48px;color:var(--white)}
  .service-24__label{font-weight:900;font-size:22px;color:var(--red)}

  .ribbon{position:absolute;left:0;display:flex;align-items:center;padding-left:33px;border-radius:0 22px 22px 0;white-space:nowrap}
  .ribbon__light{font-weight:300}
  .ribbon__bold{font-weight:900}

  .feature{position:absolute;width:150px;text-align:center}
  .feature__icon{width:66px;height:66px;margin:0 auto;display:block}
  .feature__title{font-weight:700;font-size:24px;margin-top:14px}
  .feature__text{font-size:12px;line-height:1.25;margin-top:6px}

  .contact{position:absolute;left:0;bottom:0;width:560px;height:128px}
  .contact__address{position:absolute;left:20px;top:30px;display:flex;align-items:center;gap:8px;font-size:11px;line-height:1.25;white-space:nowrap}
  .contact__pin{width:20px;height:26px;flex:none}
  .contact__phone{position:absolute;top:26px;width:226px;height:35px;border:3px solid var(--white);border-radius:18px;display:flex;align-items:center;justify-content:center;font-size:24px;font-weight:700}
  .contact__web{position:absolute;left:88px;top:68px;display:flex;align-items:center;gap:8px;font-size:32px;font-weight:700}
  .contact__globe{width:26px;height:26px}

  .intro{position:absolute;left:207px;top:128px;width:452px;font-size:20px;line-height:25px}
  .extras{position:absolute;left:40px;top:338px;list-style:none}
  .extras__item{display:flex;gap:10px;margin-bottom:8px}
  .extras__icon{width:28px;height:28px;flex:none}
  .extras__title{font-weight:900;font-size:20px;line-height:26px;text-transform:uppercase}
  .extras__text{font-size:20px;line-height:24px}
</style>
</head>
<body>

<section class="postcard postcard--front">
  <svg class="postcard__shapes" viewBox="0 0 1070 642" aria-hidden="true">
    <rect width="1070" height="642" fill="var(--black)"/>
    <path d="M598 0 L742 158 Q760 182 742 206 L520 513" fill="none" stroke="var(--white)" stroke-width="14"/>
    <path d="M0 0 H598 L742 158 Q760 182 742 206 L520 513 H0 Z" fill="var(--red)"/>
  </svg>
  <div class="postcard__photo" role="img" aria-label="Photo of a white motor yacht's bow cutting through the sea at sunset"></div>
  <svg class="postcard__shapes" viewBox="0 0 1070 642" aria-hidden="true">
    <line x1="900" y1="0" x2="436" y2="642" stroke="var(--white)" stroke-width="16"/>
  </svg>

  <div class="brand-block"><span class="brand-block__name">HARBOR<br>MATES</span></div>

  <div class="headline-line headline-line--main" style="left:196px;top:30px;width:430px;font-size:74px">We Offer</div>
  <div class="headline-line headline-line--sub" style="left:196px;top:108px;width:430px;font-size:37px">Bespoke Services</div>
  <div class="headline-line headline-line--tag" style="left:196px;top:150px;width:430px;font-size:27px;line-height:36px">Refit and update your yacht,<br>compliment any system.</div>
  <div class="dotted-rule" style="left:252px;top:230px;width:318px"></div>

  <div class="service-24">
    <div class="service-24__num">24/7</div>
    <div class="service-24__label">SERVICE</div>
  </div>

  <div class="ribbon" style="top:265px;width:618px;height:43px;background:var(--black);font-size:34px">
    <span class="ribbon__light">FAIR &amp; FRIENDLY&nbsp;</span><span class="ribbon__bold">YACHT SERVICE</span>
  </div>

  <div class="feature" style="left:15px;top:322px">
    <svg class="feature__icon" viewBox="0 0 66 66"><circle cx="33" cy="33" r="31" fill="none" stroke="var(--white)" stroke-width="3"/><path d="M27 42 V24 L41 21 V38" fill="none" stroke="var(--white)" stroke-width="3"/><circle cx="24" cy="42" r="4" fill="var(--white)"/><circle cx="38" cy="38" r="4" fill="var(--white)"/></svg>
    <div class="feature__title">Audio</div>
    <div class="feature__text">We perform most projects<br>in-house, and when we use<br>sub-cons we only use<br>the best.</div>
  </div>
  <div class="feature" style="left:191px;top:322px">
    <svg class="feature__icon" viewBox="0 0 66 66"><circle cx="33" cy="33" r="31" fill="none" stroke="var(--white)" stroke-width="3"/><path d="M18 33 Q33 20 48 33 Q33 46 18 33 Z" fill="var(--white)"/><circle cx="33" cy="33" r="5" fill="var(--red)"/></svg>
    <div class="feature__title">Visual</div>
    <div class="feature__text">TV's on custom lifts<br>and fold outs.<br>Smart TV's Media Servers<br>and more.</div>
  </div>
  <div class="feature" style="left:348px;top:322px">
    <svg class="feature__icon" viewBox="0 0 66 66"><circle cx="33" cy="33" r="31" fill="none" stroke="var(--white)" stroke-width="3"/><path d="M19 29 Q33 17 47 29 M23 34 Q33 26 43 34 M28 39 Q33 35 38 39" fill="none" stroke="var(--white)" stroke-width="3" stroke-linecap="round"/><circle cx="33" cy="44" r="2.5" fill="var(--white)"/></svg>
    <div class="feature__title">Internet</div>
    <div class="feature__text">Domestic Connectivity<br>Marina Connectivity<br>On Board Wi-Fi</div>
  </div>

  <div class="contact">
    <div class="contact__address">
      <svg class="contact__pin" viewBox="0 0 20 26"><path d="M10 0 A9 9 0 0 1 19 9 C19 16 10 26 10 26 C10 26 1 16 1 9 A9 9 0 0 1 10 0 Z" fill="var(--red)"/><circle cx="10" cy="9" r="3.5" fill="var(--black)"/></svg>
      <span>2840 Bayview Drive, #210<br>Miami Beach, FL 33140</span>
    </div>
    <div class="contact__phone" style="left:192px;background:var(--red)">(954) 555-0172</div>
    <div class="contact__web">
      <svg class="contact__globe" viewBox="0 0 26 26"><g fill="none" stroke="var(--white)" stroke-width="2"><circle cx="13" cy="13" r="11"/><ellipse cx="13" cy="13" rx="5" ry="11"/><path d="M2 13 H24 M4 7 H22 M4 19 H22"/></g></svg>
      <span>harbormates.us</span>
    </div>
  </div>
</section>

<section class="postcard postcard--back">
  <svg class="postcard__shapes" viewBox="0 0 1070 642" aria-hidden="true">
    <defs>
      <linearGradient id="band-red" x1="0" x2="1"><stop offset="0" stop-color="var(--red)"/><stop offset="1" stop-color="var(--red-dark)"/></linearGradient>
    </defs>
    <rect width="1070" height="642" fill="var(--black)"/>
    <polygon points="600,0 950,0 700,340" fill="var(--red)"/>
    <path d="M635 0 L750 128 Q768 152 750 178 L510 515" fill="none" stroke="var(--white)" stroke-width="14"/>
    <path d="M0 0 H635 L750 128 Q768 152 750 178 L510 515 H0 Z" fill="var(--black)"/>
    <rect x="0" y="515" width="600" height="127" fill="url(#band-red)"/>
  </svg>
  <div class="postcard__photo" role="img" aria-label="Aerial photo of a large white motor yacht moored at a dock"></div>
  <svg class="postcard__shapes" viewBox="0 0 1070 642" aria-hidden="true">
    <line x1="932" y1="0" x2="462" y2="642" stroke="var(--white)" stroke-width="16"/>
  </svg>

  <div class="brand-block"><span class="brand-block__name">HARBOR<br>MATES</span></div>

  <div class="headline-line headline-line--main" style="left:200px;top:18px;width:430px;font-size:50px">We Offer</div>
  <div class="headline-line headline-line--sub" style="left:200px;top:70px;width:430px;font-size:26px">Monthly Management Plans</div>
  <div class="dotted-rule" style="left:250px;top:106px;width:320px"></div>

  <p class="intro">We offer monthly management plans to ensure the vessel is ready to go at a moments notice. This can be as simple as washing once a week, or as involved as washing, waxing, detailing, provisioning &amp; crew services.</p>

  <div class="ribbon" style="top:284px;width:493px;height:40px;background:var(--red);font-size:38px;padding-left:30px">
    <span class="ribbon__light">ADDITIONAL&nbsp;</span><span class="ribbon__bold">SERVICES</span>
  </div>

  <ul class="extras">
    <li class="extras__item">
      <svg class="extras__icon" viewBox="0 0 28 28"><circle cx="14" cy="14" r="12.5" fill="none" stroke="var(--white)" stroke-width="2"/><g fill="none" stroke="var(--white)" stroke-width="2" stroke-linecap="round"><circle cx="14" cy="8" r="2"/><path d="M14 10 V21 M10 13 H18 M8 17 Q9 21 14 21 Q19 21 20 17"/></g></svg>
      <div><div class="extras__title">Voyages, Packages Sales &amp; Troubleshooting</div></div>
    </li>
    <li class="extras__item">
      <svg class="extras__icon" viewBox="0 0 28 28"><circle cx="14" cy="14" r="12.5" fill="none" stroke="var(--white)" stroke-width="2"/><g fill="none" stroke="var(--white)" stroke-width="2" stroke-linecap="round"><circle cx="14" cy="8" r="2"/><path d="M14 10 V21 M10 13 H18 M8 17 Q9 21 14 21 Q19 21 20 17"/></g></svg>
      <div><div class="extras__title">Captaining &amp; Crew</div><div class="extras__text">Captain 200 tons, Mate, and Stewardess</div></div>
    </li>
    <li class="extras__item">
      <svg class="extras__icon" viewBox="0 0 28 28"><circle cx="14" cy="14" r="12.5" fill="none" stroke="var(--white)" stroke-width="2"/><g fill="none" stroke="var(--white)" stroke-width="2" stroke-linecap="round"><circle cx="14" cy="8" r="2"/><path d="M14 10 V21 M10 13 H18 M8 17 Q9 21 14 21 Q19 21 20 17"/></g></svg>
      <div><div class="extras__title">Internet Sales</div><div class="extras__text">Coastline A/C Pumps, Stereo Packages, LED Power<br>Supplies, 220 V Appliances</div></div>
    </li>
  </ul>

  <div class="contact">
    <div class="contact__address">
      <svg class="contact__pin" viewBox="0 0 20 26"><path d="M10 0 A9 9 0 0 1 19 9 C19 16 10 26 10 26 C10 26 1 16 1 9 A9 9 0 0 1 10 0 Z" fill="var(--white)"/><circle cx="10" cy="9" r="3.5" fill="var(--red)"/></svg>
      <span>2840 Bayview Drive, #210<br>Miami Beach, FL 33140</span>
    </div>
    <div class="contact__phone" style="left:192px;background:var(--black)">(954) 555-0172</div>
    <div class="contact__web">
      <svg class="contact__globe" viewBox="0 0 26 26"><g fill="none" stroke="var(--white)" stroke-width="2"><circle cx="13" cy="13" r="11"/><ellipse cx="13" cy="13" rx="5" ry="11"/><path d="M2 13 H24 M4 7 H22 M4 19 H22"/></g></svg>
      <span>harbormates.us</span>
    </div>
  </div>
</section>

</body>
</html>
```